Qorvant Flyer Design Project

We need a new flyer design for our company based in Australia. We provide Business Valuations for small businesses. The flyer should follow the same colours and theme as our website www.qorvant.com.au and our logo. The design should communicate a professional financial services company. It should be a simple design (not too 'busy') and have a sleek and professional feel to it. It will be used to send to prospective clients and referral sources to tell about our company and prompt them to call us or visit our website.

Target Market(s)

Business owners and people working in financial services (accountants, financial planners etc)

Industry/Entity Type

Financial

Requirements
Must have
• Must be DL double sided, (99mm x 210mm) and use CMYK colours. Must contain trim marks for printer and be print ready.

```html
<!DOCTYPE html>
<html lang="en">
<head>
<meta charset="utf-8">
<title>Qorvant DL Flyer – Front and Back</title>
<link href="https://fonts.googleapis.com/css2?family=PT+Sans:wght@700&family=Tinos:wght@400;700&display=swap" rel="stylesheet">
<style>
  :root {
    --paper: #ffffff;
    --ink: #111111;
    --brand-purple: #3b3a8f;
    --brand-navy: #2a2870;
    --deep-blue: #1f2a7a;
    --mid-blue: #3a5cb0;
    --sky-blue: #4f8fd0;
    --pale-blue: #dbe8f6;
    --night: #151a26;
    --night-2: #2a3242;
    --step-blue: #2f5ea8;
    --step-light: #8fb4e4;
    --white: #ffffff;
  }
  * { margin: 0; padding: 0; box-sizing: border-box; }
  html, body {
    width: 1143px; height: 1200px; overflow: hidden;
    background: var(--paper);
  }
  .sheet { position: relative; width: 1143px; height: 1200px; }

  .side-label {
    position: absolute; top: 30px; width: 464px; text-align: center;
    font-family: "Tinos", "Times New Roman", serif; font-weight: 700;
    font-size: 46px; color: var(--ink);
  }
  .side-label--front { left: 78px; }
  .side-label--back { left: 588px; }

  .panel {
    position: absolute; top: 138px; width: 464px; height: 976px; overflow: hidden;
  }
  .panel--front { left: 78px; }
  .panel--back { left: 588px; }
  .panel__art { position: absolute; inset: 0; }

  .brand-name {
    position: absolute; font-family: "PT Sans", Arial, sans-serif; font-weight: 700;
    color: var(--brand-purple); letter-spacing: 1px;
  }
  .serif { font-family: "Tinos", "Times New Roman", serif; font-weight: 700; color: var(--white); }

  /* Front */
  .front__name { top: 142px; left: 0; width: 464px; text-align: center; font-size: 52px; }
  .front__headline {
    position: absolute; top: 212px; left: 20px; width: 440px;
    font-family: "PT Sans", Arial, sans-serif; font-weight: 700;
    font-size: 38px; line-height: 47px; color: var(--white);
  }
  .front__headline span { display: block; }
  .front__headline .l1 { padding-left: 12px; }
  .front__headline .l2 { padding-left: 58px; }
  .front__headline .l3 { padding-left: 96px; }
  .front__headline .l4 { padding-left: 104px; }
  .front__pitch {
    position: absolute; top: 584px; left: 0; width: 464px; text-align: center;
    font-size: 28px; line-height: 35px;
  }
  .front__cta { position: absolute; left: 0; width: 464px; text-align: center; }
  .front__cta--touch { top: 782px; font-size: 28px; }
  .front__cta--web { top: 830px; font-size: 36px; }
  .front__cta--phone { top: 888px; font-size: 52px; letter-spacing: 1px; }

  /* Back */
  .back__name { top: 104px; left: 54px; font-size: 50px; }
  .back__web { position: absolute; top: 178px; left: 12px; font-size: 21px; color: var(--brand-navy); }
  .back__title {
    position: absolute; top: 284px; left: 0; width: 390px; text-align: center;
    font-family: "Tinos", "Times New Roman", serif; font-weight: 400;
    font-size: 35px; line-height: 48px; color: var(--white);
  }
  .step-tag {
    position: absolute; width: 196px; height: 32px;
    background: linear-gradient(180deg, var(--step-light), var(--step-blue) 55%, var(--deep-blue));
    font-family: "PT Sans", Arial, sans-serif; font-weight: 700; font-size: 25px;
    line-height: 32px; color: var(--white); text-align: center;
  }
  .step-tag--1 { left: 26px; top: 398px; }
  .step-tag--2 { left: 238px; top: 580px; }
  .step-tag--3 { left: 26px; top: 786px; }
  .step-text {
    position: absolute; font-family: "Tinos", "Times New Roman", serif; font-weight: 400;
    font-size: 25px; line-height: 36px; color: var(--white); text-align: center; width: 320px;
  }
  .step-text--1 { left: 20px; top: 436px; }
  .step-text--2 { left: 102px; top: 624px; }
  .step-text--3 { left: 62px; top: 838px; }
</style>
</head>
<body>
<main class="sheet">
  <h2 class="side-label side-label--front">front</h2>
  <h2 class="side-label side-label--back">back</h2>

  <!-- Front side -->
  <section class="panel panel--front">
    <svg class="panel__art" width="464" height="976" viewBox="0 0 464 976">
      <defs>
        <linearGradient id="frontPhoto" x1="0" y1="0" x2="1" y2="1">
          <stop offset="0" stop-color="#2a3690"/>
          <stop offset="0.45" stop-color="#6c86c6"/>
          <stop offset="0.75" stop-color="#c8d2e6"/>
          <stop offset="1" stop-color="#1c2030"/>
        </linearGradient>
        <linearGradient id="frontBase" x1="0" y1="0" x2="0" y2="1">
          <stop offset="0" stop-color="#1f2a7a"/>
          <stop offset="0.45" stop-color="#34489e"/>
          <stop offset="1" stop-color="#4f8fd0"/>
        </linearGradient>
      </defs>
      <rect x="0" y="0" width="464" height="560" fill="url(#frontPhoto)" role="img" aria-label="Photo of city office towers and a hand signing a financial document"/>
      <path d="M0 490 C120 470 200 540 300 530 C380 522 430 470 464 460 L464 976 L0 976 Z" fill="url(#frontBase)"/>
      <path d="M0 490 C120 470 200 540 300 530 C380 522 430 470 464 460" fill="none" stroke="#6fa6e0" stroke-width="3" opacity="0.6"/>
      <circle cx="232" cy="82" r="58" fill="#3b3a8f"/>
    </svg>
    <div class="brand-name front__name">Qorvant</div>
    <h1 class="front__headline">
      <span class="l1">Before you buy or</span>
      <span class="l2">sell a business</span>
      <span class="l3">Let us check</span>
      <span class="l4">the numbers</span>
    </h1>
    <p class="serif front__pitch">Invest in our expertise<br>and gain peace of<br>mind with our Fixed Price<br>Business Valuation Report</p>
    <p class="serif front__cta front__cta--touch">Get In Touch With Us</p>
    <p class="serif front__cta front__cta--web">www.qorvant.com.au</p>
    <p class="serif front__cta front__cta--phone">1300 482 657</p>
  </section>

  <!-- Back side -->
  <section class="panel panel--back">
    <svg class="panel__art" width="464" height="976" viewBox="0 0 464 976">
      <defs>
        <linearGradient id="backTop" x1="0" y1="0" x2="0" y2="1">
          <stop offset="0" stop-color="#7fa8d8"/>
          <stop offset="1" stop-color="#e4eef8"/>
        </linearGradient>
        <linearGradient id="backBase" x1="0" y1="0" x2="0" y2="1">
          <stop offset="0" stop-color="#2a3242"/>
          <stop offset="0.5" stop-color="#1a2030"/>
          <stop offset="1" stop-color="#151a26"/>
        </linearGradient>
        <linearGradient id="portrait" x1="0" y1="0" x2="0" y2="1">
          <stop offset="0" stop-color="#e8eef6"/>
          <stop offset="1" stop-color="#3a3f4c"/>
        </linearGradient>
      </defs>
      <rect x="0" y="0" width="464" height="300" fill="url(#backTop)"/>
      <rect x="272" y="0" width="192" height="286" fill="url(#portrait)" role="img" aria-label="Photo of a smiling business adviser in a suit with arms crossed"/>
      <path d="M0 296 C90 250 200 250 300 270 C380 284 430 268 464 250 L464 976 L0 976 Z" fill="url(#backBase)"/>
      <circle cx="128" cy="68" r="58" fill="#3b3a8f"/>
      <line x1="190" y1="534" x2="238" y2="562" stroke="#3a5cb0" stroke-width="2"/>
      <path d="M228 562 L240 563 L234 553" fill="none" stroke="#3a5cb0" stroke-width="2"/>
      <line x1="218" y1="712" x2="166" y2="770" stroke="#3a5cb0" stroke-width="2"/>
      <path d="M166 758 L165 771 L177 767" fill="none" stroke="#3a5cb0" stroke-width="2"/>
    </svg>
    <div class="brand-name back__name">Qorvant</div>
    <p class="serif back__web">www.qorvant.com.au</p>
    <h2 class="back__title">We Follow Three<br>Simple Steps</h2>
    <div class="step-tag step-tag--1">STEP-1</div>
    <p class="step-text step-text--1">Provide information<br>about the business</p>
    <div class="step-tag step-tag--2">STEP-2</div>
    <p class="step-text step-text--2">A qualified Accountant<br>analyses the business.</p>
    <div class="step-tag step-tag--3">STEP-3</div>
    <p class="step-text step-text--3">Your valuation Report<br>is emailed to you.</p>
  </section>
</main>
</body>
</html>
```